BHSC Business cards

We are an established dental practice that is looking for new business cards to match our new logo. We are looking for something unique and sophisticated.
BRIEF: Colours are black, silver and white. Include the company name, logo (including “Pelwick Heath Dental Care”) and phone number “03 9415 2876”.
Front - Include the company name, logo (including “Pelwick Heath Dental Care”) and phone number “03 9415 2876”.
Back - Include the company name,  “Pelwick Heath Dental Care”, phone number “03 9415 2876”. address "64A Tindle Street, Pelwick Heath, Vic 3187", "Email reception@pelwickheathdentalcare.com.au", the Dentist Name " Dr ................................"  Your next appointment "Day, date and time(am/pm)".  3 lines for 3 appointments please, and at the bottom "IF UNABLE TO KEEP THIS APPOINTMENT 48 HOURS NOTICE IS REQUIRED."
Try and be creative and different with the design, i've added an image for inspiration

Target Market(s)
ALL in need of dental
Industry/Entity Type
Dental Clinic
Look and feel
Each slider illustrates characteristics of the customer's brand and the style your logo design should communicate.

```html
<!DOCTYPE html>
<html lang="en">
<head>
<meta charset="utf-8">
<title>Pelwick Heath Dental Care – Business Cards</title>
<link rel="stylesheet" href="https://fonts.googleapis.com/css2?family=Jost:wght@400;500;600&family=Montserrat:wght@400&display=swap">
<style>
  :root {
    --backdrop: #2e2e2e;
    --card-white: #ffffff;
    --silver: #e6e6e6;
    --silver-mark: #e4e4e4;
    --ink: #1a1a1a;
    --ink-soft: #333333;
    --band: #1c1c1c;
    --band-text: #ffffff;
  }
  * { margin: 0; padding: 0; box-sizing: border-box; }
  html, body { width: 1200px; height: 1059px; overflow: hidden; }
  body {
    background: var(--backdrop);
    font-family: "Jost", sans-serif;
    color: var(--ink);
    position: relative;
  }
  .card {
    position: absolute;
    background: var(--card-white);
    border-radius: 24px;
    overflow: hidden;
  }
  .card--front { left: 256px; top: 100px; width: 688px; height: 391px; }
  .card--back  { left: 253px; top: 537px; width: 694px; height: 394px; }

  .brand { position: absolute; display: flex; align-items: center; }
  .brand__dot { border-radius: 50%; background: var(--ink); flex: none; }
  .brand__name {
    font-family: "Jost", sans-serif;
    font-weight: 600;
    text-transform: uppercase;
    color: var(--ink);
    line-height: 1.02;
    letter-spacing: 0.04em;
  }
  .brand__phone {
    position: absolute;
    font-family: "Jost", sans-serif;
    font-weight: 500;
    color: var(--ink);
    letter-spacing: 0.08em;
  }

  /* front */
  .card--front .brand { left: 30px; top: 129px; }
  .card--front .brand__dot { width: 56px; height: 56px; margin-right: 14px; }
  .card--front .brand__name { font-size: 21px; }
  .card--front .brand__phone { left: 100px; top: 183px; font-size: 11px; }
  .front-phone { position: absolute; left: 30px; top: 222px; display: flex; align-items: center; }
  .front-phone__icon {
    width: 40px; height: 40px; border-radius: 50%; background: var(--ink);
    display: flex; align-items: center; justify-content: center; margin-right: 13px;
  }
  .front-phone__number {
    font-family: "Montserrat", sans-serif; font-size: 31px; color: var(--ink-soft);
  }
  .front-mark {
    position: absolute; left: 378px; top: 39px; width: 296px; height: 296px;
    border-radius: 50%; background: var(--silver-mark);
  }

  /* back */
  .back-panel { position: absolute; left: 0; top: 0; width: 411px; height: 100%; background: var(--silver); }
  .dentist { position: absolute; left: 23px; top: 50px; }
  .dentist__name { font-size: 24px; font-weight: 500; line-height: 1.2; }
  .dentist__role { font-size: 18px; font-weight: 400; color: var(--ink-soft); }
  .address { position: absolute; left: 23px; top: 181px; font-size: 16px; line-height: 20px; color: var(--ink-soft); }
  .contacts { position: absolute; left: 23px; top: 236px; list-style: none; font-size: 16px; color: var(--ink-soft); }
  .contacts li { display: flex; align-items: center; height: 24.5px; }
  .contacts svg { margin-right: 6px; flex: none; }

  .card--back .brand { left: 423px; top: 49px; }
  .card--back .brand__dot { width: 44px; height: 44px; margin-right: 10px; }
  .card--back .brand__name { font-size: 16px; }
  .card--back .brand__phone { left: 477px; top: 91px; font-size: 9px; }

  .appointments { position: absolute; left: 423px; top: 126px; width: 246px; }
  .appointments__title { font-size: 13px; color: var(--ink); letter-spacing: 0.01em; }
  .appointments__line { border-bottom: 1px dashed #555; height: 24px; margin-top: 9px; }
  .appointments__line + .appointments__line { margin-top: 9px; }
  .slots { margin-top: 28px; list-style: none; font-size: 11.5px; color: var(--ink-soft); }
  .slots li { display: flex; align-items: baseline; height: 28px; }
  .slots .fill { border-bottom: 1px dashed #555; width: 72px; margin: 0 4px; }
  .notice {
    position: absolute; left: 0; top: 333px; width: 100%; height: 38px;
    background: var(--band); color: var(--band-text);
    display: flex; align-items: center; justify-content: center;
    font-size: 15.5px; letter-spacing: 0.01em;
  }
</style>
</head>
<body>

<section class="card card--front" aria-label="Card front">
  <div class="front-mark" role="img" aria-label="Faint brand circle decoration"></div>
  <div class="brand">
    <span class="brand__dot"></span>
    <span class="brand__name">Pelwick Heath<br>Dental Care</span>
  </div>
  <span class="brand__phone">03 9415 2876</span>
  <div class="front-phone">
    <span class="front-phone__icon">
      <svg width="20" height="20" viewBox="0 0 24 24" fill="#fff"><path d="M6.6 10.8a15.1 15.1 0 0 0 6.6 6.6l2.2-2.2a1 1 0 0 1 1-.25 11.4 11.4 0 0 0 3.6.57 1 1 0 0 1 1 1V20a1 1 0 0 1-1 1A17 17 0 0 1 3 4a1 1 0 0 1 1-1h3.5a1 1 0 0 1 1 1c0 1.25.2 2.45.57 3.57a1 1 0 0 1-.25 1z"/></svg>
    </span>
    <span class="front-phone__number">03 9415 2876</span>
  </div>
</section>

<section class="card card--back" aria-label="Card back">
  <div class="back-panel"></div>
  <div class="dentist">
    <p class="dentist__name">Dr Marcus Elwyn</p>
    <p class="dentist__role">Dentist</p>
  </div>
  <p class="address">64A Tindle Street,<br>Pelwick Heath, Vic 3187</p>
  <ul class="contacts">
    <li><svg width="14" height="14" viewBox="0 0 24 24" fill="#222"><path d="M6.6 10.8a15.1 15.1 0 0 0 6.6 6.6l2.2-2.2a1 1 0 0 1 1-.25 11.4 11.4 0 0 0 3.6.57 1 1 0 0 1 1 1V20a1 1 0 0 1-1 1A17 17 0 0 1 3 4a1 1 0 0 1 1-1h3.5a1 1 0 0 1 1 1c0 1.25.2 2.45.57 3.57a1 1 0 0 1-.25 1z"/></svg>03 9415 2876</li>
    <li><svg width="14" height="11" viewBox="0 0 24 18"><rect x="1" y="1" width="22" height="16" fill="#222"/><path d="M1 1l11 9 11-9" stroke="#e6e6e6" stroke-width="2" fill="none"/></svg>reception@pelwickheathdentalcare.com.au</li>
    <li><svg width="14" height="14" viewBox="0 0 24 24"><circle cx="12" cy="12" r="10" fill="#222"/><path d="M2 12h20M12 2c3 3 3 17 0 20M12 2c-3 3-3 17 0 20" stroke="#e6e6e6" stroke-width="1.5" fill="none"/></svg>pelwickheathdentalcare.com.au</li>
  </ul>

  <div class="brand">
    <span class="brand__dot"></span>
    <span class="brand__name">Pelwick Heath<br>Dental Care</span>
  </div>
  <span class="brand__phone">03 9415 2876</span>

  <div class="appointments">
    <p class="appointments__title">NEXT APPOINTMENT</p>
    <div class="appointments__line"></div>
    <div class="appointments__line"></div>
    <ul class="slots">
      <li>Date<span class="fill"></span>At<span class="fill"></span>am/pm</li>
      <li>Date<span class="fill"></span>At<span class="fill"></span>am/pm</li>
      <li>Date<span class="fill"></span>At<span class="fill"></span>am/pm</li>
    </ul>
  </div>

  <p class="notice">IF UNABLE TO KEEP THIS APPOINTMENT 48 HOURS NOTICE IS REQUIRED</p>
</section>

</body>
</html>
```